Cover for new song release

Song title: “Paper Lantern”. It’s a song about being in the moment. (Verse lyrics: “You can have your eyes wide open and still not even know...For every two steps forward take Paper Lantern and take in all the beauty all around.”

```html
<!DOCTYPE html>
<html lang="en">
<head>
<meta charset="utf-8">
<title>Paper Lantern — Song Cover</title>
<link rel="stylesheet" href="https://fonts.googleapis.com/css2?family=IM+Fell+DW+Pica&display=swap">
<style>
  :root {
    --sky-top: #7b505b;
    --sky-low: #8e5e6c;
    --haze-pink: #d9a3ad;
    --haze-lilac: #d3b8e4;
    --neon-violet: #a57fd6;
    --city-blue: #5a5c9e;
    --city-dusk: #3d2a4a;
    --ember: #f0a53a;
    --ember-deep: #b8561f;
    --rock: #1d1315;
    --band: #140a0c;
    --title-ink: #fbf6f2;
  }
  * { margin: 0; padding: 0; box-sizing: border-box; }
  html, body {
    width: 1200px;
    height: 1200px;
    overflow: hidden;
    background: var(--band);
  }
  .cover {
    position: relative;
    width: 1200px;
    height: 1200px;
    overflow: hidden;
    background: var(--band);
    font-family: "IM Fell DW Pica", Georgia, serif;
  }
  .cover__scene {
    position: absolute;
    left: 0;
    top: 0;
    width: 1200px;
    height: 1060px;
    background:
      radial-gradient(ellipse 40% 9% at 48% 91%, rgba(240, 165, 58, 0.85), rgba(184, 86, 31, 0.35) 55%, transparent 80%),
      radial-gradient(ellipse 30% 14% at 72% 82%, rgba(240, 165, 58, 0.45), transparent 75%),
      radial-gradient(ellipse 35% 16% at 62% 52%, rgba(236, 222, 245, 0.75), transparent 75%),
      radial-gradient(ellipse 22% 10% at 92% 44%, rgba(200, 110, 230, 0.6), transparent 75%),
      radial-gradient(ellipse 45% 9% at 18% 37%, rgba(240, 175, 185, 0.7), transparent 75%),
      radial-gradient(ellipse 30% 7% at 80% 35%, rgba(50, 30, 55, 0.55), transparent 75%),
      radial-gradient(ellipse 50% 22% at 30% 70%, rgba(120, 95, 190, 0.5), transparent 75%),
      radial-gradient(ellipse 90% 14% at 50% 100%, var(--rock) 55%, transparent 90%),
      linear-gradient(
        to bottom,
        var(--sky-top) 0%,
        var(--sky-low) 24%,
        #a9788a 32%,
        var(--haze-pink) 38%,
        var(--haze-lilac) 48%,
        var(--neon-violet) 58%,
        var(--city-blue) 68%,
        var(--city-dusk) 80%,
        #2a1a22 90%,
        var(--rock) 97%,
        var(--band) 100%
      );
  }
  .cover__title {
    position: absolute;
    top: 104px;
    left: 0;
    right: 0;
    text-align: center;
    font-size: 112px;
    font-weight: 400;
    line-height: 1;
    color: var(--title-ink);
    letter-spacing: 1px;
  }
  .cover__artist {
    position: absolute;
    top: 1096px;
    left: 0;
    right: 0;
    text-align: center;
    font-size: 68px;
    font-weight: 400;
    line-height: 1;
    color: var(--title-ink);
  }
</style>
</head>
<body>
  <main class="cover">
    <div class="cover__scene" role="img"
         aria-label="Woman with long hair seen from behind, carrying an acoustic guitar, standing on a rocky outcrop above a misty neon-lit city at night, with a pale moon and glowing embers rising around her"></div>
    <h1 class="cover__title">Paper Lantern</h1>
    <p class="cover__artist">Singer Name</p>
  </main>
</body>
</html>
```